Tarnwick auto buffing and headlight restoration

I'm offering a service the will restore dull and discoloured headlights caused by sun damage. I also want to offer minor scratch repairs. $25 per headlight $10-$30 for scratches Mobile serviceI'd like to have an example of a dull and a new headlight. Clean colours eg. Blues,silver and whites.Very clean uncomplicated and professionals looking card. I'd like it to have a bold logo.

Target Market(s)

All car, truck and vehicle owners. Automotive industries.

Industry/Entity Type

Automotive

Contact Information for Business Card

(Front)
Headlight restoration and scratch Repair
Marcus Tarnwick
Mobile-0412 986 240
(Back)
Pricing
$25 per headlight
$10-$35 per scratch

Font styles to use
Sans Serif

Colors
85cae6
ffffff
0355a3
faa54b

Requirements
Must have
• Logo
• I would like my name to look confident. As if to say "I back myself"
• Bold easy to read text
• Clean lines
• Name -Marcus Tarnwick
• Phone- txt or call 0412986240
• Email- 61marct@mailvexo.com
Nice to have
• I'm open to other color schemes
• 4 color scheme only
• Minimal orange
• Small amount of Silver if possible
• Bold outlined logo
Should not have
• Complex lines and logos

```html
<!DOCTYPE html>
<html lang="en">
<head>
<meta charset="utf-8">
<title>Tarnwick auto buffing and headlight restoration – Pricing card</title>
<link rel="stylesheet" href="https://fonts.googleapis.com/css2?family=Questrial&display=swap">
<style>
  :root {
    --backdrop: #e4e6e8;
    --card-blue: #3ea6d2;
    --white: #ffffff;
    --stripe: rgba(255, 255, 255, 0.45);
    --card-shadow: rgba(0, 0, 0, 0.25);
  }
  * { margin: 0; padding: 0; box-sizing: border-box; }
  html, body {
    width: 1200px;
    height: 1000px;
    overflow: hidden;
  }
  body {
    background: var(--backdrop);
    font-family: "Questrial", "Century Gothic", sans-serif;
    position: relative;
  }
  .pricing-card {
    position: absolute;
    left: 80px;
    top: 185px;
    width: 1040px;
    height: 630px;
    background: var(--card-blue);
    color: var(--white);
    box-shadow: 0 4px 10px var(--card-shadow);
  }
  .heading-stripes {
    position: absolute;
    top: 128px;
    height: 62px;
  }
  .heading-stripes--left { left: 0; width: 372px; }
  .heading-stripes--right { left: 668px; width: 372px; }
  .card-title {
    position: absolute;
    top: 122px;
    left: 0;
    width: 100%;
    text-align: center;
    font-size: 72px;
    font-weight: 400;
    line-height: 1;
  }
  .price-list {
    position: absolute;
    top: 296px;
    left: 0;
    width: 100%;
    list-style: none;
    text-align: center;
    font-size: 38px;
    line-height: 67px;
  }
  .brand-name {
    position: absolute;
    top: 508px;
    left: 0;
    width: 100%;
    text-align: center;
    font-size: 34px;
    line-height: 1;
    color: var(--white);
  }
</style>
</head>
<body>
  <section class="pricing-card" aria-label="Pricing">
    <svg class="heading-stripes heading-stripes--left" viewBox="0 0 372 62" aria-hidden="true">
      <g fill="var(--stripe)">
        <rect x="0" y="0" width="372" height="4"/>
        <rect x="0" y="14" width="372" height="4"/>
        <rect x="0" y="29" width="372" height="4"/>
        <rect x="0" y="43" width="372" height="4"/>
        <rect x="0" y="58" width="372" height="4"/>
      </g>
    </svg>
    <h1 class="card-title">Pricings</h1>
    <svg class="heading-stripes heading-stripes--right" viewBox="0 0 372 62" aria-hidden="true">
      <g fill="var(--stripe)">
        <rect x="0" y="0" width="372" height="4"/>
        <rect x="0" y="14" width="372" height="4"/>
        <rect x="0" y="29" width="372" height="4"/>
        <rect x="0" y="43" width="372" height="4"/>
        <rect x="0" y="58" width="372" height="4"/>
      </g>
    </svg>
    <ul class="price-list">
      <li>$25 per headlight</li>
      <li>$10-$35 per scratch</li>
    </ul>
    <p class="brand-name">Tarnwick</p>
  </section>
</body>
</html>
```